依頼詳細
★★★ランディングページに必ず入れて欲しい文言です★★★
----------------------------------
■キャッチ
ページ制作5ページ+問い合わせフォーム+初期費用
通常価格:149,100円(税込)
6/28までの限定キャンペーン!!先着10名まで!!

キャンペーン価格63,000円(税込み)
※初期費用は、ドメイン取得代行・レンタルサーバ取得代行を含みます。
※ページ制作は5ページまでとなります。
※ドメイン代<年額:850円~>、レンタルサーバ代<年額4,725円~>は別途お客様にてご負担頂きます。
※ホームページに掲載する画像を撮影することも可能です(但し、別途費用が発生します)

■3つのポイント
1.SEOで上位表示を行います
2.PC・スマートフォンに最適化されたページを提供します
3.納品後のサポート6ヶ月無料サービス付き

■問い合わせフォーム

サイトURL
harblume.co.jp
ページ数
1ページ
希望イメージ
シンプル 複雑
単色 カラフル
暗い 明るい
日常 高級
遊び心 厳粛
未来的 伝統的
女性的 男性的
希望する色
青、オレンジ、白
納品ファイル
• 高解像度JPG (.jpg)
• イラストレーター形式 (.ai)
• フォトショップ形式 (.psd)
• PNG形式 (.png)
補足説明
■ 重視する点/検討基準
・予算
・ランディングページ(LP)を作成をした経験
・過去のランディングページ(LP)作成実績を公開して頂けること
・LPOを意識したデザインをして頂けること
・ランディングページ(LP)をリスティングで利用した経験

■ 利用用途
Vantoro Bidlinesのリンク先として使用します。

■ 納品形式
各レイヤー毎に分かれたpsdファイルで納品をお願いします。
■ 選んだ理由

第一印象が想像していたランディングページに近かった為。

■ 提案者全員のお礼・コメント

この度は弊社のランディングページへのご提案ありがとうございました。

修正依頼なども快く引き受けて頂き、すばらしいランディングページができました。
早速コーディングに入りたいと思います。

この度は本当にありがとうございました。

```html
<!DOCTYPE html>
<html lang="ja">
<head>
<meta charset="utf-8">
<title>harblume キャンペーン</title>
<link href="https://fonts.googleapis.com/css2?family=Noto+Sans+JP:wght@400;500;700;900&display=swap" rel="stylesheet">
<style>
:root{
  --blue:#2a8fd8;
  --blue-dark:#1668b0;
  --blue-light:#d9eef9;
  --orange:#f08a1c;
  --orange-dark:#e0620a;
  --red:#e0281e;
  --ink:#333;
  --navy:#1d2a3a;
  --grey:#666;
  --white:#fff;
}
*{margin:0;padding:0;box-sizing:border-box}
html,body{width:1200px;height:2856px;overflow:hidden}
body{font-family:"Noto Sans JP",sans-serif;color:var(--ink);background:var(--white);position:relative}
.abs{position:absolute}

.header{left:0;top:0;width:1200px;height:112px;background:var(--white)}
.brand{left:36px;top:22px;display:flex;align-items:center;gap:14px}
.brand-mark{width:52px;height:52px;border-radius:50%;background:var(--blue)}
.brand-name{font-size:40px;font-weight:700;color:var(--blue-dark);line-height:1}
.brand-tag{left:102px;top:74px;font-size:13px;color:var(--grey)}

.hero{left:0;top:112px;width:1200px;height:1138px;background:linear-gradient(180deg,#cfe9f8 0%,#eef8fd 40%,#f7fbfe 100%);overflow:hidden}
.package{left:40px;top:30px;width:1120px;display:flex;align-items:center;justify-content:center;gap:12px;white-space:nowrap}
.package .pill{background:linear-gradient(180deg,#49a9ea,var(--blue-dark));color:var(--white);font-size:36px;font-weight:700;padding:6px 26px;border-radius:6px}
.package .plus{font-size:42px;font-weight:700;color:var(--blue-dark)}

.limited{left:70px;top:128px;color:var(--red);font-size:38px;font-weight:900;line-height:1.25;text-align:center;transform:rotate(-6deg);white-space:nowrap;z-index:3}
.regular{left:450px;top:180px;font-size:26px;font-weight:700;color:var(--ink);white-space:nowrap;z-index:3}
.regular b{font-size:44px;font-weight:900}
.first{left:880px;top:124px;font-size:36px;font-weight:900;color:var(--red);transform:rotate(-8deg);white-space:nowrap;z-index:3}
.arrow{left:600px;top:244px;z-index:3}
.campaign{left:0;top:262px;width:1200px;text-align:center;color:var(--orange);font-weight:900;font-size:48px;line-height:1;white-space:nowrap;z-index:3}
.campaign b{font-size:120px;letter-spacing:1px}

.photo{left:640px;top:360px;width:520px;height:760px;background:linear-gradient(180deg,#f4f6f8,#dfe5ea);z-index:1}

.points-title{left:72px;top:388px;width:380px;height:90px;background:linear-gradient(180deg,#f59a2c,var(--orange-dark));color:var(--white);font-size:48px;font-weight:900;display:flex;align-items:center;padding-left:32px;border-radius:4px;z-index:2}
.point{left:72px;width:720px;height:160px;background:var(--white);border:2px solid #c6dced;border-radius:6px;z-index:2}
.point .num{position:absolute;left:22px;top:14px;font-size:100px;font-weight:400;font-style:normal;color:var(--blue);line-height:1}
.point .text{position:absolute;left:120px;right:20px;top:0;bottom:0;display:flex;flex-direction:column;justify-content:center;align-items:center;font-size:36px;font-weight:700;line-height:1.35;text-align:center;white-space:nowrap}
.p1{top:528px}.p2{top:708px}.p3{top:888px}

.notes{left:0;top:1250px;width:1200px;height:250px;background:#f3f8fb;padding:50px 80px;font-size:20px;line-height:1.85;color:var(--ink)}

.form-section{left:0;top:1500px;width:1200px;height:1356px;background:linear-gradient(180deg,#2c8fd6 0%,#7cc3ee 6%,#e6f4fc 14%,#ffffff 50%,#cfe8f7 90%,#2c8fd6 100%)}
.form-heading{left:0;top:70px;width:1200px;text-align:center;font-size:44px;font-weight:900;color:var(--navy);white-space:nowrap}
.form-box{left:120px;top:170px;width:960px;height:1070px;background:var(--white);border:1px solid #d8e4ec}
.intro{left:40px;top:44px;font-size:20px;line-height:1.9;color:var(--ink)}
.form-table{left:20px;top:190px;width:920px;border-collapse:collapse}
.form-table td{border-bottom:1px solid #c9dfee;height:80px;font-size:20px}
.form-table td.label{width:320px;background:var(--blue-light);padding-left:20px}
.form-table td.field{padding-left:30px}
.req{display:inline-block;background:var(--red);color:var(--white);font-size:14px;padding:2px 10px;margin-right:18px}
.input{height:36px;width:420px;border:1px solid #bbb;background:var(--white)}
.input.area{height:110px;width:420px}
.row-tall td{height:150px}
.submit{left:280px;top:900px;width:400px;height:80px;background:linear-gradient(180deg,#f7a23a,var(--orange-dark));border-radius:8px;color:var(--white);font-size:30px;font-weight:700;display:flex;align-items:center;justify-content:center}
.copyright{left:0;top:1290px;width:1200px;text-align:center;font-size:16px;color:var(--white)}
</style>
</head>
<body>

<header class="header abs">
  <div class="brand abs"><span class="brand-mark"></span><span class="brand-name">harblume</span></div>
  <div class="brand-tag abs">Web Design Studio</div>
</header>

<section class="hero abs">
  <div class="package abs">
    <span class="pill">ページ制作5ページ</span><span class="plus">+</span>
    <span class="pill">問い合わせフォーム</span><span class="plus">+</span>
    <span class="pill">初期費用</span>
  </div>
  <div class="limited abs">6/28までの<br>限定キャンペーン!!</div>
  <div class="regular abs">通常価格<b>149,100</b>円（税込）</div>
  <div class="first abs">先着10名まで!!</div>
  <svg class="arrow abs" width="70" height="24" viewBox="0 0 70 24"><polygon points="0,0 70,0 35,24" fill="var(--blue)"/></svg>
  <div class="campaign abs">キャンペーン価格<b>63,000</b>円（税込）</div>

  <div class="photo abs" role="img" aria-label="書類を持ち指差しする女性スタッフの写真"></div>

  <div class="points-title abs">3つのポイント</div>
  <div class="point p1 abs"><i class="num">1</i><div class="text">SEOで上位表示を行います</div></div>
  <div class="point p2 abs"><i class="num">2</i><div class="text">PC・スマートフォンに<br>最適化されたページを提供します</div></div>
  <div class="point p3 abs"><i class="num">3</i><div class="text">納品後のサポート<br>6ヶ月無料サービス付き</div></div>
</section>

<div class="notes abs">
  ※初期費用は、ドメイン取得代行・レンタルサーバ取得代行を含みます。<br>
  ※ページ制作は5ページまでとなります。<br>
  ※ドメイン代&lt;年額:850円~&gt;、レンタルサーバ代&lt;年額4,725円~&gt;は別途お客様にてご負担頂きます。<br>
  ※ホームページに掲載する画像を撮影することも可能です（但し、別途費用が発生します）
</div>

<section class="form-section abs">
  <h2 class="form-heading abs">下記フォームよりお気軽にお問い合わせください</h2>
  <div class="form-box abs">
    <p class="intro abs">下記項目に必要事項を明記し、送信してください。<br>後ほど担当者からご連絡いたします。<br>提供された個人情報は、第三者に公開されることはありません。</p>
    <table class="form-table abs">
      <tr><td class="label"><span class="req">必須</span>氏名（全角）</td><td class="field"><div class="input"></div></td></tr>
      <tr><td class="label"><span class="req">必須</span>フリガナ（全角）</td><td class="field"><div class="input"></div></td></tr>
      <tr><td class="label"><span class="req">必須</span>電話番号</td><td class="field"><div class="input"></div></td></tr>
      <tr><td class="label"><span class="req">必須</span>メールアドレス</td><td class="field"><div class="input"></div></td></tr>
      <tr><td class="label"><span class="req">必須</span>確認用メールアドレス</td><td class="field"><div class="input"></div></td></tr>
      <tr class="row-tall"><td class="label"><span class="req">必須</span>お問い合わせ内容</td><td class="field"><div class="input area"></div></td></tr>
    </table>
    <div class="submit abs">入力内容を確認 ›</div>
  </div>
  <p class="copyright abs">Copyright (C) harblume All Rights Reserved.</p>
</section>

</body>
</html>
```